Double Gate Fold Brochure for Medical Center

We need an elegant design for a double-gate fold brochure for a medical center.
- Logo is attached
- Output must be in .AI format
- Brand colors is gold/light brown, as used in the logo
- The print template for 14"x 8.5" double-gate brochure is attached. (zip)
- Below is a link to content and images. Please be creative about the layouts, effect and placements.

https://slides.vornatek.net/deck/q/7Qv-2KmT_w9XrLp0aZc3HhE5nYbU4sJdFgMi1oRtS8y/open?mode=sharing

```html
<!DOCTYPE html>
<html lang="en">
<head>
<meta charset="utf-8">
<title>Calder &amp; Vale Surgical Institute – Gate Fold Brochure</title>
<link href="https://fonts.googleapis.com/css2?family=Libre+Baskerville&family=Open+Sans:wght@400;600&display=swap" rel="stylesheet">
<style>
  :root {
    --gold: #a9936b;
    --gray: #8b8c90;
    --paper: #f3f3f3;
    --white: #ffffff;
    --ink: #3c3c3c;
    --canvas: #d9dadc;
    --serif: "Libre Baskerville", Georgia, serif;
    --sans: "Open Sans", Arial, sans-serif;
  }
  * { margin: 0; padding: 0; box-sizing: border-box; }
  html, body { width: 962px; height: 1200px; overflow: hidden; }
  body { background: var(--canvas); font-family: var(--sans); color: var(--ink); position: relative; }

  .spread { position: absolute; left: 55px; width: 850px; height: 521px; background: var(--paper);
            box-shadow: 0 4px 8px rgba(0,0,0,.18); overflow: hidden; }
  .spread--outside { top: 54px; }
  .spread--inside { top: 627px; }
  .spread svg.art { position: absolute; inset: 0; width: 850px; height: 521px; z-index: 0; }

  .block, .brand, .contact, .liaison { position: absolute; z-index: 1; }
  .block { font-size: 6.8px; line-height: 1.42; }
  .heading { font-family: var(--serif); font-size: 10.5px; line-height: 1.25; color: var(--gold);
             text-transform: uppercase; margin-bottom: 6px; }
  .heading--light { color: var(--white); }
  .sub { color: var(--gold); margin: 7px 0 4px; }
  .on-gold, .on-gray { color: var(--white); }
  p + p { margin-top: 7px; }
  .justify { text-align: justify; }

  ul { list-style: none; }
  .dot-list li { padding-left: 6px; position: relative; margin-bottom: 3px; }
  .dot-list li::before { content: "•"; position: absolute; left: 0; color: var(--gold); }
  .arrow-list li { padding-left: 11px; position: relative; margin-bottom: 3.4px; }
  .arrow-list li::before { content: "›"; position: absolute; left: 0; top: 1px; width: 6px; height: 6px;
    border: .7px solid currentColor; border-radius: 50%; font-size: 6px; line-height: 4.6px; text-align: center; }
  .on-paper .arrow-list li::before { color: var(--gold); }

  .site { font-size: 10px; letter-spacing: .8px; color: var(--white); text-align: center; }

  .brand { text-align: center; font-family: var(--serif); color: var(--gold); }
  .brand__name { display: block; }
  .brand__tag { display: block; text-transform: uppercase; }
  .brand--white { color: var(--white); }

  .contact { left: 425px; width: 212px; top: 418px; text-align: center; color: var(--white); }
  .contact .heading { margin-bottom: 7px; }
  .contact__addr { font-size: 7.8px; line-height: 1.45; }
  .phone-pill { display: inline-flex; align-items: center; gap: 8px; margin: 5px 0 6px; background: #e9e9e9;
    color: var(--gold); border-radius: 10px; padding: 1px 30px; font-size: 12px; }
  .phone-pill svg { width: 11px; height: 11px; }

  .specialties { display: grid; grid-template-columns: 1fr 1fr; column-gap: 4px; }
  .specialties li { margin-bottom: 3px; }
  .partner-note { color: var(--gold); margin-top: 8px; }
  .perks { margin-top: 10px; border-top: .6px dashed #bfbfbf; color: var(--gold); font-size: 6.2px; }
  .perks div { display: flex; border-bottom: .6px dashed #bfbfbf; }
  .perks span { flex: 1; text-align: center; padding: 4px 0; }
  .perks span + span { border-left: .6px dashed #bfbfbf; }

  .liaison { left: 651px; top: 440px; display: flex; gap: 8px; font-size: 6.4px; line-height: 1.35; }
  .liaison__photo { width: 55px; height: 65px; background: linear-gradient(#9a9ea4, #5f6368); }
  .liaison__name { margin-top: 5px; }
  .liaison__line { display: flex; align-items: center; gap: 3px; }
  .liaison__line i { width: 6px; height: 6px; border-radius: 50%; background: var(--gold); display: inline-block; }
</style>
</head>
<body>

<section class="spread spread--outside">
  <svg class="art" viewBox="0 0 850 521">
    <defs>
      <linearGradient id="room" x1="0" y1="0" x2="0" y2="1"><stop offset="0" stop-color="#f4f5f6"/><stop offset="1" stop-color="#c9ccd1"/></linearGradient>
      <linearGradient id="team" x1="0" y1="0" x2="0" y2="1"><stop offset="0" stop-color="#e9ecef"/><stop offset="1" stop-color="#7ea6c8"/></linearGradient>
      <linearGradient id="night" x1="0" y1="0" x2="0" y2="1"><stop offset="0" stop-color="#1f2b4a"/><stop offset="1" stop-color="#3e5078"/></linearGradient>
      <linearGradient id="dusk" x1="0" y1="0" x2="0" y2="1"><stop offset="0" stop-color="#b9c6dc"/><stop offset="1" stop-color="#5f6f86"/></linearGradient>
    </defs>
    <path role="img" aria-label="Photo: bright clinic reception area with front desk" d="M0,0 H212 V116 C150,122 60,132 0,144 Z" fill="url(#room)"/>
    <path d="M0,144 C60,132 150,122 212,116 V126 C150,132 60,142 0,154 Z" fill="var(--gray)"/>
    <path d="M0,344 C70,330 150,324 212,322 V521 H0 Z" fill="var(--gold)"/>
    <path role="img" aria-label="Photo: waiting lounge with white sofas and artwork" d="M0,358 C70,344 150,338 212,336 V521 H0 Z" fill="url(#room)"/>
    <rect role="img" aria-label="Photo: surgical team in blue scrubs" x="212" y="0" width="213" height="150" fill="url(#team)"/>
    <path d="M212,142 C290,132 360,146 425,140 V420 H212 Z" fill="var(--gold)"/>
    <rect x="425" y="0" width="212" height="170" fill="var(--white)"/>
    <path role="img" aria-label="Photo: glass office building at night" d="M425,162 C500,178 580,150 637,140 V420 H425 Z" fill="url(#night)"/>
    <path role="img" aria-label="Photo: private recovery room with hospital bed" d="M637,0 H850 V184 C780,188 700,190 637,196 Z" fill="url(#room)"/>
    <path d="M637,196 C700,190 780,188 850,184 V192 C780,196 700,198 637,204 Z" fill="var(--gray)"/>
    <rect x="637" y="204" width="213" height="210" fill="var(--white)"/>
    <path d="M212,345 C290,330 360,410 425,404 C510,400 580,410 637,412 C720,404 800,388 850,370 V521 H212 Z" fill="var(--gray)"/>
    <path d="M637,402 C720,394 800,378 850,360 V372 C800,390 720,406 637,414 Z" fill="var(--gold)"/>
    <circle cx="317" cy="376" r="57" fill="#dcdcdc"/>
    <circle role="img" aria-label="Photo: office building at dusk" cx="317" cy="376" r="52" fill="url(#dusk)"/>
  </svg>

  <div class="block on-paper" style="left:16px; top:158px; width:188px;">
    <h2 class="heading">Surgical Clinic</h2>
    <p>Conveniently located at an adjacent suit, our surgical clinic is a complement to the surgery center, and is available to surgeons under flexible programs.</p>
    <p class="sub">The surgical clinic includes:</p>
    <ul class="dot-list">
      <li>Reception and waiting area with 2 front stations</li>
      <li>5 fully-equipped exam rooms</li>
      <li>5 luxury furnished physician offices</li>
      <li>8 staff stations</li>
      <li style="font-size:6.2px">Conference room equipped with audiovisual technology</li>
      <li>Cloud-based free EMR</li>
      <li>Support staff</li>
    </ul>
  </div>

  <div class="block on-gold" style="left:226px; top:148px; width:194px;">
    <h2 class="heading heading--light">Our Team</h2>
    <p style="margin-bottom:7px">Our team of experienced staff is composed of:</p>
    <ul class="arrow-list">
      <li>Director of Operation</li>
      <li>Director of Nursing</li>
      <li>Circulating &amp; Recovery nurses with years of experience</li>
      <li>Lead Surgical Technician</li>
      <li>Experienced Surgical Technicians, trained for varieties of specialityand subspecialty procedure</li>
      <li>Physician Liaison</li>
      <li>Maintenance and supply officer</li>
      <li>All staff and BLS or ACLS certified</li>
    </ul>
  </div>

  <div class="block on-gray" style="left:226px; top:437px; width:186px; text-align:center;">
    <p>At Calder &amp; Vale we are committed to provide the highest quality of the care to our patients at our state of the art facility. Our goal is to make our patients' experience as smooth and stress free as possible. We are proudly an accredited AHQA center.</p>
    <p class="site" style="margin-top:9px">www.caldervalesurgical.com</p>
  </div>

  <div class="brand" style="left:425px; top:44px; width:212px;">
    <span class="brand__name" style="font-size:26px; line-height:1.2;">Calder &amp; Vale</span>
    <span class="brand__tag" style="font-size:11px; margin-top:24px;">Surgical Institute</span>
  </div>

  <div class="contact">
    <h2 class="heading heading--light">Contact Us</h2>
    <p class="contact__addr">4870 Linden Park Ave. Suite 210<br>Westbrook, CA 90188</p>
    <div class="phone-pill">
      <svg viewBox="0 0 12 12"><circle cx="6" cy="6" r="5.3" fill="none" stroke="currentColor" stroke-width=".9"/><path d="M4.2,3.2 L5,3 5.5,4.4 4.9,4.9 C5.2,5.8 6,6.6 6.9,6.9 L7.4,6.3 8.8,6.8 8.6,7.6 C6.6,8.2 3.6,5.2 4.2,3.2Z" fill="currentColor"/></svg>
      <span>310 555 0148</span>
    </div>
    <p class="site">www.caldervalesurgical.com</p>
  </div>

  <div class="block on-paper" style="left:651px; top:208px; width:188px; font-size:6.6px;">
    <h2 class="heading" style="font-size:9.6px;">About Calder &amp; Vale Surgical Institute</h2>
    <p class="justify">Established in 2017 and Accredited by AHQA, Calder &amp; Vale Surgical Institute is strategically located in the heart of Westbrook, at one of the most prestigious facilities in the Harbor Coast.</p>
    <p class="justify">Our facility includes 4 integrated operating rooms with state-of-the-art equipment, 8 private recovery rooms with overnight capability, 24/7 support staff and highest level of hospitality standards.</p>
    <p class="justify">Families strongly matter to us, which is why our facility is built with roomy and comfortable waiting area and various opportunities to relax and regroup.</p>
  </div>

  <div class="brand brand--white" style="left:700px; top:444px; width:150px;">
    <span class="brand__name" style="font-size:17px;">Calder &amp; Vale</span>
    <span class="brand__tag" style="font-size:7px; margin-top:16px;">Surgical Institute</span>
  </div>
</section>

<section class="spread spread--inside">
  <svg class="art" viewBox="0 0 850 521">
    <defs>
      <linearGradient id="room2" x1="0" y1="0" x2="0" y2="1"><stop offset="0" stop-color="#f4f5f6"/><stop offset="1" stop-color="#cfd2d6"/></linearGradient>
      <linearGradient id="or" x1="0" y1="0" x2="0" y2="1"><stop offset="0" stop-color="#eef0f2"/><stop offset="1" stop-color="#a9adb3"/></linearGradient>
      <linearGradient id="warm" x1="0" y1="0" x2="0" y2="1"><stop offset="0" stop-color="#eceae6"/><stop offset="1" stop-color="#c8b89a"/></linearGradient>
    </defs>
    <path role="img" aria-label="Photo: bright corridor with recovery bays" d="M0,0 H212 V140 C150,158 70,166 0,160 Z" fill="url(#room2)"/>
    <path d="M0,160 C70,166 150,158 212,140 V150 C150,170 70,178 0,172 Z" fill="var(--gold)"/>
    <rect x="212" y="0" width="425" height="330" fill="var(--gold)"/>
    <path d="M212,318 C320,300 420,300 520,312 C580,318 610,316 637,310 V330 H212 Z" fill="var(--gray)"/>
    <path role="img" aria-label="Photo: operating room with surgical table, booms and monitors" d="M212,330 C320,314 420,312 520,322 C580,328 610,326 637,322 V521 H212 Z" fill="url(#or)"/>
    <path role="img" aria-label="Photo: private recovery room with bed and armchair" d="M637,0 H850 V140 C780,150 700,148 637,118 Z" fill="url(#room2)"/>
    <path d="M637,118 C700,148 780,150 850,140 V150 C780,162 700,160 637,130 Z" fill="var(--gold)"/>
    <circle cx="106" cy="188" r="56" fill="#e2e2e2"/>
    <circle role="img" aria-label="Photo: lounge with sofas and city view" cx="106" cy="188" r="51" fill="url(#warm)"/>
  </svg>

  <div class="block on-paper" style="left:16px; top:262px; width:192px;">
    <h2 class="heading">Surgical Clinic</h2>
    <p>Established in 2017 and Accredited by AHQA, Calder &amp; Vale Surgical Institute is strategically located in heart of Harbor Coast at one of the most prestigious buildings in the area.</p>
    <p class="sub">Our 14,000 sq ft. facility includes:</p>
    <ul class="arrow-list">
      <li>4 integrated operating rooms equipped with latest technology</li>
      <li>8 private recovery rooms with overnight stay</li>
      <li>Luxurious reception area</li>
      <li>Physician lounge &amp; pantry</li>
      <li>Spacious recreational outdoor patio</li>
    </ul>
  </div>

  <div class="brand" style="left:60px; top:446px; width:92px;">
    <span class="brand__name" style="font-size:13px;">Calder &amp; Vale</span>
    <span class="brand__tag" style="font-size:6px; margin-top:18px;">Surgical Institute</span>
  </div>

  <div class="block on-gold" style="left:226px; top:34px; width:200px;">
    <h2 class="heading heading--light">Equipment</h2>
    <p class="justify" style="margin-bottom:8px">We are proud to offer our physicians the latest in surgical technology:</p>
    <ul class="arrow-list">
      <li>Integrated laparoscopic equipment</li>
      <li>5K resolution camera head</li>
      <li>4K, 32" boom monitors</li>
      <li>Onsite radiology &amp; fluoroscopy</li>
      <li>Integrated endoscopy suite</li>
      <li>VisiCam video laryngoscope</li>
      <li>Fiberoptic laryngoscope</li>
      <li>Solvix A6 Portable Ultrasound</li>
      <li>Advanced laparoscopic and arthroscopic instruments</li>
      <li>Tidal Rover Suction/ Irrigation systems</li>
      <li>Central gas system</li>
      <li>Hospital grade beds in recovery rooms</li>
      <li>Fully implemented EMR</li>
      <li>Onsite dictation software</li>
    </ul>
  </div>

  <div class="block on-gold" style="left:437px; top:34px; width:190px;">
    <h2 class="heading heading--light">Hospitality</h2>
    <ul class="arrow-list">
      <li>8 private recovery rooms equipped with</li>
      <li>hospital grade beds and cable TV and apps</li>
      <li>Overnight and extended stay capability for patient comfort</li>
      <li>24/7 support staff</li>
      <li>Transfer agreement with an advanced closeby hospital</li>
      <li>Dedicated physician liaison</li>
      <li>Complimentary stay for physicians and patients at the next-door Harborview hotel</li>
      <li>Courtesy transportations to/from facility for surgeons and patients</li>
      <li>Free parking for physicians, staff, patients and families.</li>
      <li>Walking distance to Bayfront Fashion Center</li>
      <li>Center, Hotels and Restaurants</li>
    </ul>
  </div>

  <div class="block on-paper" style="left:650px; top:188px; width:190px;">
    <h2 class="heading">Physician Advantage</h2>
    <p style="margin-bottom:7px">Calder &amp; Vale is your facility of choice for:</p>
    <ul class="arrow-list specialties">
      <li>General Surgery</li><li>Plastic &amp; Reconstructive</li>
      <li>Bariatric Surgery</li><li>Hand Surgery</li>
      <li>Gynecology</li><li>Pediatric Surgery</li>
      <li>Urology</li><li>Podiatric Surgery</li>
      <li>Orthopedics</li><li>Head and Neck Surgery</li>
      <li>Spine Surgery</li><li>ENT</li>
      <li>Pain management</li><li>Colon &amp; Rectal Surgery</li>
    </ul>
    <p class="partner-note">Our "Physician Partnership Program" are structured by one of the most respected healthcare law firms in the region</p>
    <div class="perks">
      <div><span>No Buy-In required</span><span>No Non-Compete Clause</span></div>
      <div><span>No Long-Term Commitment</span><span>Guaranteed Membership Status</span></div>
      <div><span>No-membership fee</span></div>
    </div>
  </div>

  <div class="liaison">
    <div class="liaison__photo" role="img" aria-label="Portrait photo of the Director of Operation"></div>
    <div>
      <p>For more information about Physician<br>Partnership Programs, please contact:</p>
      <p class="liaison__name">Marcus Delano, MBA<br>Director of Operation</p>
      <p class="liaison__line" style="margin-top:3px"><i></i>310 555 0148</p>
      <p class="liaison__line"><i></i>m.delano@caldervalesurgical.com</p>
    </div>
  </div>
</section>

</body>
</html>
```